STYLISH

It will be a brochure that exemplifies a project to make a modern and avant-garde LEGAL MAGAZINE to "sell it" to the sponsors, it will be a legal niche magazine for lawyers. The style is of the type "The Velvet Drum" of the lawyers, breaks scheme, more disruptive More alternative with innovative personality and that calls the attention. It will be a collection magazine, to look at the reception of the Legal Firms. For public between 27 and 45 years. The name of the Magazine will be EL VERGEL

Target Market(s)

Chilean Lawyers between 27 and 45 years old.

Industry/Entity Type

Legal

Logo Text

EL VERGEL

Font styles to use
Sans Serif

Colors

Designer to choose colors to be used in the design.

Requirements
Must have
• Must say the name of the Magazine EL VERGEL Elevate the lawyer by giving him a different "coolness". We make them look and feel cool Elevate the lawyer to a public figure. They have something important to say. Our covers reflect that. A lawyer's study in a rich, unique session. The lawyer should be at the center of all our sections. They always in the middle. They are our protagonists.
Nice to have
• Minimalist, cool, fine. 1. With the white border like MORDANTE MAGAZINE attached. 2. The cover must have the photograph with the pictures of the opposite attached .. 3. Name ok the magazine: THE GROVE 4. On the left footer the word: COLLECTION | 01 5. On the write footer: THE MOST PRESTIGIOUS ATTORNEY ACCORDING TO HALLORAN & BRECK
Should not have
• information saturation

```html
<!DOCTYPE html>
<html lang="en">
<head>
<meta charset="utf-8">
<title>EL VERGEL — Magazine Spread</title>
<link rel="stylesheet" href="https://fonts.googleapis.com/css2?family=Montserrat:wght@700&family=Arimo:wght@400&display=swap">
<style>
  :root {
    --page-white: #ffffff;
    --panel-slate: #414b54;
    --accent-copper: #c48c55;
    --text-light: #f4f4f4;
    --figure-dark: #2f3033;
    --figure-mid: #3a3b3f;
  }
  * { margin: 0; padding: 0; box-sizing: border-box; }
  html, body {
    width: 1200px;
    height: 800px;
    overflow: hidden;
    background: var(--page-white);
  }
  .spread {
    position: relative;
    width: 1200px;
    height: 800px;
  }
  .page {
    position: absolute;
    top: 24px;
    width: 528px;
    height: 738px;
    background: var(--panel-slate);
    overflow: hidden;
  }
  .page--cover { left: 67px; }
  .page--article { left: 604px; }
  .cover-art, .article-title, .corner-mark {
    position: absolute;
    left: 0;
    top: 0;
  }
  .masthead-text {
    font-family: "Montserrat", sans-serif;
    font-weight: 700;
  }
  .copper { fill: var(--accent-copper); }
  .white { fill: var(--page-white); }
  .article-body {
    position: absolute;
    left: 24px;
    top: 254px;
    width: 480px;
    font-family: "Arimo", sans-serif;
    font-size: 18.8px;
    line-height: 21px;
    color: var(--text-light);
    white-space: nowrap;
  }
  .article-body p + p { margin-top: 21px; }
</style>
</head>
<body>
<main class="spread">

  <section class="page page--cover">
    <svg class="cover-art" width="528" height="738" viewBox="0 0 528 738">
      <text class="masthead-text copper" x="13" y="142" font-size="140" textLength="515" lengthAdjust="spacingAndGlyphs">EL VERGEL</text>
      <path class="white" d="M9 738 A256 256 0 0 1 521 738 L470 738 A205 205 0 0 0 60 738 Z"/>
      <defs>
        <linearGradient id="figureTone" x1="0" y1="0" x2="0" y2="1">
          <stop offset="0" stop-color="#3a3b3f"/>
          <stop offset="1" stop-color="#2f3033"/>
        </linearGradient>
      </defs>
      <rect role="img" aria-label="Illustration of a bearded lawyer in a dark suit and red tie standing at the centre of the cover" x="149" y="88" width="216" height="620" rx="40" fill="url(#figureTone)"/>
    </svg>
  </section>

  <section class="page page--article">
    <svg class="article-title" width="528" height="260" viewBox="0 0 528 260">
      <text class="masthead-text copper" x="12" y="224" font-size="256" textLength="224" lengthAdjust="spacingAndGlyphs">EL</text>
      <text class="masthead-text" x="140" y="224" font-size="137" textLength="350" lengthAdjust="spacingAndGlyphs"><tspan class="white">VE</tspan><tspan class="copper">RGEL</tspan></text>
    </svg>

    <article class="article-body">
      <p>Lorem Ipsum is simply dummy text of the printing and<br>typesetting industry. Lorem Ipsum has been the<br>industry's standard dummy text ever since the 1500s,<br>when an unknown printer took a galley of type and<br>scrambled it to make a type specimen book. It has<br>survived not only five centuries, but also the leap into<br>electronic typesetting, remaining essentially<br>unchanged. It was popularised in the 1960s with the<br>release of Typewell sheets containing Lorem Ipsum<br>passages, and more recently with desktop publishing<br>software like Folio LayoutDesk including versions of<br>Lorem Ipsum.</p>
      <p>Why do we use it?<br>It is a long established fact that a reader will be<br>distracted by the readable content of a page when<br>looking at its layout. The point of using Lorem Ipsum is<br>that it has a more-or-less normal distribution of letters,<br>as opposed to using 'Content here, content here',<br>making it look like readable English. Many desktop</p>
    </article>

    <svg class="corner-mark" width="528" height="738" viewBox="0 0 528 738" aria-hidden="true">
      <rect class="copper" x="482" y="629" width="13" height="72"/>
      <rect class="copper" x="436" y="688" width="59" height="13"/>
    </svg>
  </section>

</main>
</body>
</html>
```